Corona rapid test station

We need a banner for a container. This container will stand in the pedestrian zone of a large city. What is required is high-quality graphics with pictures of people who draw the eye, but also fit the topic of the Corona rapid test. One possible theme is the portrayal of young people getting tested to protect their older relatives.

Corona rapid test, result within 15 minutes
Pre-registration by phone: 0648/27 584 6

Leave empty field for price.

The umbrella brand should be clearly visible: Lindwurm-Apotheken (Attention, an n must be added to the existing logo: Lindwurm-Apotheken <-)

The branches are to be listed smaller: Lindwurm-Apotheke, Birk-Apotheke, Solveig-Apotheke, Tamara-Apotheke

Format: 2m high, 5.5m wide

Target Market(s)

People between 20 and 60 years of age

Requirements
Must have
• The logo of the umbrella brand Lindwurm-Apotheken stands above everything. The design of the central pharmacies (green / blue) is reflected in the overall design.
Font Nexa Bold or Nexa light
Nice to have
• Faces of people without a mask

```html
<!DOCTYPE html>
<html lang="en">
<head>
<meta charset="utf-8">
<title>Rapid Test Container Banner</title>
<link rel="stylesheet" href="https://fonts.googleapis.com/css2?family=Montserrat:wght@800&family=Mulish:wght@300;700&family=Oswald:wght@600&family=Playfair+Display:wght@800&display=swap">
<style>
  :root {
    --page: #e9ebee;
    --ink: #111111;
    --paper: #ffffff;
    --green: #6cb33f;
    --green-dark: #1f6b2c;
    --green-fill: #e3f1d6;
    --blue: #1b8bc7;
    --blue-deep: #1d6f9a;
    --navy: #23406b;
    --photo-dark: #0a0a0a;
    --photo-mid: #3a4a55;
  }
  * { margin: 0; padding: 0; box-sizing: border-box; }
  html, body { width: 1200px; height: 1200px; overflow: hidden; background: var(--page); }
  .banner {
    position: absolute; left: 30px; top: 340px;
    width: 1140px; height: 520px;
    background: var(--paper);
    overflow: hidden;
    box-shadow: 0 6px 24px rgba(0,0,0,.15);
  }
  .banner__art { position: absolute; inset: 0; }
  .banner__content {
    position: absolute; left: 360px; right: 20px; top: 0; bottom: 0;
    display: flex; flex-direction: column; align-items: center;
  }
  .umbrella {
    margin-top: 16px;
    display: flex; align-items: center; gap: 10px;
    font-family: "Mulish", sans-serif; font-weight: 700;
    font-size: 28px; line-height: 34px; letter-spacing: 1px; color: var(--navy);
    white-space: nowrap;
  }
  .umbrella__dot { width: 22px; height: 22px; border-radius: 50%; background: var(--green); }
  .headline {
    margin-top: 12px;
    font-family: "Montserrat", sans-serif; font-weight: 800;
    font-size: 56px; letter-spacing: -1.5px; line-height: 1;
    white-space: nowrap;
    color: var(--green-fill);
    -webkit-text-stroke: 2px var(--green-dark);
    paint-order: stroke fill;
  }
  .subline {
    margin-top: 18px;
    font-family: "Mulish", sans-serif; font-weight: 300;
    font-size: 44px; letter-spacing: -1px; line-height: 1;
    color: var(--navy); white-space: nowrap;
  }
  .subline em { font-style: normal; color: var(--blue); }
  .prereg {
    margin-top: 26px;
    font-family: "Oswald", sans-serif; font-weight: 600;
    font-size: 28px; line-height: 1; color: var(--ink); white-space: nowrap;
  }
  .phone {
    margin-top: 6px;
    font-family: "Playfair Display", serif; font-weight: 800;
    font-size: 64px; line-height: 1; color: var(--blue-deep); white-space: nowrap;
  }
  .price-field {
    margin-top: 22px;
    width: 260px; height: 78px;
    border: 3px solid var(--blue);
    border-radius: 10px;
    background: var(--paper);
  }
  .branches {
    position: absolute; left: 0; right: 0; bottom: 24px;
    display: flex; justify-content: space-around; align-items: center;
    font-family: "Mulish", sans-serif; font-weight: 700;
    font-size: 16px; color: var(--navy); white-space: nowrap;
  }
  .branch { display: flex; align-items: center; gap: 6px; }
  .branch__mark { width: 12px; height: 12px; border-radius: 50%; background: var(--blue); }
</style>
</head>
<body>
  <section class="banner">
    <svg class="banner__art" width="1140" height="520" viewBox="0 0 1140 520">
      <defs>
        <linearGradient id="photoTone" x1="0" y1="0" x2="1" y2="0">
          <stop offset="0" stop-color="var(--photo-mid)"/>
          <stop offset="0.55" stop-color="#1c2a33"/>
          <stop offset="1" stop-color="var(--photo-dark)"/>
        </linearGradient>
      </defs>
      <path role="img" aria-label="Photo: person in a white coat with a medical mask raising a gloved hand in a stop gesture on a black background"
            d="M0 0 H345 C300 130 300 220 330 330 C350 410 345 470 330 520 H0 Z" fill="url(#photoTone)"/>
      <path class="band band--green" d="M345 0 C300 130 300 220 330 330" fill="none" stroke="var(--green)" stroke-width="14"/>
      <path class="band band--blue" d="M330 330 C350 410 345 470 330 520" fill="none" stroke="var(--blue)" stroke-width="12"/>
    </svg>

    <div class="banner__content">
      <div class="umbrella"><span class="umbrella__dot"></span>LINDWURM APOTHEKEN</div>
      <h1 class="headline">CORONA RAPID TEST</h1>
      <p class="subline">RESULT WITHIN <em>15 MINUTES</em></p>
      <p class="prereg">PRE-REGISTRATION BY PHONE:</p>
      <p class="phone">0648/27 584 6</p>
      <div class="price-field" role="img" aria-label="Empty field for the price"></div>
      <div class="branches">
        <span class="branch"><span class="branch__mark"></span>Lindwurm-Apotheke</span>
        <span class="branch">Birk-Apotheke</span>
        <span class="branch">Solveig-Apotheke</span>
        <span class="branch">Tamara-Apotheke</span>
      </div>
    </div>
  </section>
</body>
</html>
```